Asia Hotel need a card and logo

The new hotel in East Asia, Taiwan need a business card and logo design.The hotel's Chinese name is 岚溪文旅,English name is "Virel Hotel".The core concept of this hotel is "Eco green", going to use many plant etc.,The building's first outlook draft is attached in the file for your reference.The style be modern and fashion will be good. Thank you.
Target Market(s)
East Asia
Industry/Entity Type
Hotel
Contact Information for Business Card
The hotel's name both in Chinese and English :岚溪商旅 Virel Hotel
The logo, address, E-mail and tel number place.
Stuff's name and title.
Font styles to use
Colors
Designer to choose colors to be used in the design.
Look and feel
Each slider illustrates characteristics of the customer's brand and the style your logo design should communicate.

```html
<!DOCTYPE html>
<html lang="en">
<head>
<meta charset="utf-8">
<title>Virel Hotel – Business Card</title>
<link href="https://fonts.googleapis.com/css2?family=Libre+Baskerville:wght@700&family=Noto+Sans+TC:wght@300&display=swap" rel="stylesheet">
<style>
  :root {
    --stage-green: #0aad74;
    --divider: #1b3a30;
    --card-dark: #1f2326;
    --leaf-green: #178c37;
    --paper: #ffffff;
    --icon-navy: #1c3557;
    --ink-light: #ffffff;
  }
  html, body {
    margin: 0;
    padding: 0;
    overflow: hidden;
  }
  .canvas {
    position: relative;
    width: 1200px;
    height: 1000px;
    background: var(--stage-green);
    overflow: hidden;
  }
  .divider-band {
    position: absolute;
    left: 0;
    top: 486px;
    width: 1200px;
    height: 26px;
    background: var(--divider);
  }
  .card {
    position: absolute;
    overflow: hidden;
    box-shadow: 4px 6px 10px rgba(0, 0, 0, 0.35);
  }
  .card-front {
    left: 259px;
    top: 56px;
    width: 679px;
    height: 386px;
    background: var(--paper);
  }
  .card-back {
    left: 239px;
    top: 552px;
    width: 699px;
    height: 396px;
    background: var(--card-dark);
  }
  .card-shape {
    position: absolute;
    left: 0;
    top: 0;
  }
  .contact-icon {
    position: absolute;
    left: 32px;
    width: 40px;
    height: 40px;
  }
  .icon-pin { top: 68px; }
  .icon-phone { top: 171px; }
  .icon-mail { top: 279px; }
  .brand-mark {
    position: absolute;
    width: 150px;
    height: 150px;
    display: flex;
    align-items: center;
    justify-content: center;
    border: 4px solid var(--ink-light);
    border-radius: 50%;
    box-sizing: border-box;
    color: var(--ink-light);
    font-family: "Libre Baskerville", serif;
    font-weight: 700;
    font-size: 34px;
  }
  .card-front .brand-mark { left: 456px; top: 54px; }
  .card-back .brand-mark { left: 466px; top: 63px; }
  .brand-name {
    position: absolute;
    width: 320px;
    text-align: center;
    color: var(--ink-light);
    font-family: "Libre Baskerville", serif;
    font-weight: 700;
    font-size: 36px;
    line-height: 1;
    margin: 0;
  }
  .brand-name-zh {
    position: absolute;
    width: 320px;
    text-align: center;
    color: var(--ink-light);
    font-family: "Noto Sans TC", sans-serif;
    font-weight: 300;
    font-size: 32px;
    letter-spacing: 1px;
    line-height: 1;
    margin: 0;
  }
  .card-front .brand-name { left: 374px; top: 241px; }
  .card-front .brand-name-zh { left: 374px; top: 289px; }
  .card-back .brand-name { left: 384px; top: 253px; }
  .card-back .brand-name-zh { left: 384px; top: 301px; }
  .bottle-panel {
    position: absolute;
    left: 0;
    top: 0;
    width: 397px;
    height: 396px;
    background: linear-gradient(90deg, var(--leaf-green) 0%, #1a5a2f 50%, var(--leaf-green) 100%);
  }
</style>
</head>
<body>
<main class="canvas">

  <section class="card card-front">
    <svg class="card-shape" width="679" height="386" viewBox="0 0 679 386" aria-hidden="true">
      <path d="M430 0 Q254 193 438 386 L679 386 L679 0 Z" fill="var(--leaf-green)"/>
      <path d="M441 0 Q295 193 413 386 L679 386 L679 0 Z" fill="var(--card-dark)"/>
    </svg>

    <svg class="contact-icon icon-pin" viewBox="0 0 40 40" aria-label="Address">
      <path d="M20 4 C12 4 7 10 7 16 C7 25 20 37 20 37 C20 37 33 25 33 16 C33 10 28 4 20 4 Z" fill="var(--icon-navy)"/>
      <circle cx="20" cy="16" r="5" fill="var(--paper)"/>
    </svg>
    <svg class="contact-icon icon-phone" viewBox="0 0 40 40" aria-label="Phone">
      <path d="M10 6 L16 6 L18 14 L14 17 C16 23 20 27 24 29 L27 25 L35 28 L35 33 C35 35 33 36 31 36 C18 35 6 23 5 10 C5 8 7 6 10 6 Z" fill="var(--icon-navy)"/>
    </svg>
    <svg class="contact-icon icon-mail" viewBox="0 0 40 40" aria-label="Email">
      <rect x="1" y="9" width="38" height="23" fill="var(--icon-navy)"/>
      <path d="M3 11 L20 23 L37 11" fill="none" stroke="var(--paper)" stroke-width="2"/>
      <path d="M3 30 L15 20 M37 30 L25 20" fill="none" stroke="var(--paper)" stroke-width="1.5"/>
    </svg>

    <div class="brand-mark">Virel</div>
    <h1 class="brand-name">Virel Hotel</h1>
    <p class="brand-name-zh" lang="zh-Hant">岚溪商旅</p>
  </section>

  <div class="divider-band"></div>

  <section class="card card-back">
    <div class="bottle-panel" role="img" aria-label="Green bottle silhouettes on dark ground"></div>
    <div class="brand-mark">Virel</div>
    <h2 class="brand-name">Virel Hotel</h2>
    <p class="brand-name-zh" lang="zh-Hant">岚溪商旅</p>
  </section>

</main>
</body>
</html>
```